Can Design for Fun, Growing Health Food Brand

We are launching a brand new product, electrolyte seltzer drinks. We want the design to be clean/simple and slightly modern while staying true to our brand identity. Must say "Mineral Hydration" as the product descriptor, sub headline is "Carbonated electrolyte beverage with sea moss and real fruit juice". First flavors will be Watermelon Mint and Mango.

Target Market(s)

Women ages 30-50 who are interested in health wellness/trends

Industry/Entity Type

Health & Wellness

Font styles to use
Sans Serif

Requirements
Must have
• Tall, skinny can, current Bright Kelp Co Logo, use aluminum on can as element in design.
Nice to have
• Be fun, clean and modern. Would like to see the label less busy than our gels.
Should not have
• Avoid putting flavor on bottom 1/5 of can. No gradient color changes. Do not want really detailed or realistic fruit image, prefer drawings or similar.

```html
<!DOCTYPE html>
<html lang="en">
<head>
<meta charset="UTF-8">
<title>Bright Kelp Co – Mineral Hydration Can Wrap</title>
<link href="https://fonts.googleapis.com/css2?family=Bebas+Neue&family=Oswald:wght@300;400;500&family=Josefin+Sans:wght@400&display=swap" rel="stylesheet">
<style>
  :root {
    --page: #ffffff;
    --aluminum-pink: #efc3b8;
    --kelp-green: #3b7447;
    --deep-green: #2d6238;
    --cream: #f2f1e6;
    --sub-green: #6f9c78;
    --melon-red: #c8262c;
    --mango-orange: #d7801a;
    --fruit-tone: #e4b447;
    --badge-text: #e3ebe2;
  }
  * { margin: 0; padding: 0; box-sizing: border-box; }
  html, body { width: 1200px; height: 1200px; overflow: hidden; background: var(--page); }

  .can-wrap {
    position: absolute; left: 240px; top: 40px;
    width: 720px; height: 1120px;
    background: var(--aluminum-pink);
  }
  .label {
    position: absolute; left: 180px; top: 110px;
    width: 360px; height: 900px;
    background: var(--cream);
    overflow: hidden;
  }
  .label svg.bands { position: absolute; inset: 0; }

  .brand {
    position: absolute; top: 0; left: 0; width: 100%;
    text-align: center; color: var(--cream);
  }
  .brand-mark {
    position: absolute; left: 157px; top: 42px;
    width: 46px; height: 46px; border-radius: 50%;
    border: 2px solid var(--cream);
  }
  .brand-name {
    position: absolute; top: 98px; width: 100%;
    font-family: "Oswald", sans-serif; font-weight: 400;
    font-size: 38px; letter-spacing: -0.5px; line-height: 1;
  }

  .descriptor {
    position: absolute; top: 192px; width: 100%; text-align: center;
    font-family: "Bebas Neue", sans-serif; font-weight: 400;
    color: var(--deep-green); line-height: 1;
  }
  .descriptor .line-1 { display: block; font-size: 78px; height: 70px; }
  .descriptor .line-2 { display: block; font-size: 66px; }

  .subhead {
    position: absolute; top: 322px; width: 100%; text-align: center;
    font-family: "Josefin Sans", sans-serif; font-size: 21px; line-height: 28px;
    color: var(--sub-green);
  }

  .fruit-art {
    position: absolute; left: 96px; top: 432px;
    width: 184px; height: 156px; border-radius: 40px;
    background: var(--fruit-tone);
  }

  .flavor {
    position: absolute; top: 602px; width: 100%; text-align: center;
    font-family: "Bebas Neue", sans-serif; font-weight: 400; line-height: 1;
  }
  .flavor .primary { display: block; font-size: 66px; color: var(--melon-red); }
  .flavor .secondary { display: block; font-size: 33px; color: var(--deep-green); }
  .flavor .mango { color: var(--mango-orange); }

  .badges {
    position: absolute; top: 748px; left: 0; width: 100%;
    list-style: none;
    display: flex; justify-content: space-between; padding: 0 30px;
  }
  .badge { width: 100px; text-align: center; }
  .badge svg { display: block; margin: 0 auto 8px; }
  .badge-text {
    font-family: "Oswald", sans-serif; font-weight: 300; font-size: 15px;
    line-height: 16px; color: var(--badge-text);
  }
  .volume {
    position: absolute; top: 856px; width: 100%; text-align: center;
    font-family: "Oswald", sans-serif; font-weight: 300; font-size: 19px;
    letter-spacing: 1px; color: var(--badge-text);
  }
</style>
</head>
<body>
  <div class="can-wrap" role="img" aria-label="Aluminum can wrap with a red line pattern of watermelon slices and mint leaves">
    <div class="label">
      <svg class="bands" width="360" height="900" viewBox="0 0 360 900" aria-hidden="true">
        <path d="M0 0 H360 V150 C320 140 290 150 260 165 C215 185 165 160 120 150 C70 140 35 165 0 168 Z" fill="var(--kelp-green)"/>
        <path d="M0 738 C40 728 75 716 120 710 C160 705 185 720 225 724 C265 728 300 712 360 740 V900 H0 Z" fill="var(--kelp-green)"/>
      </svg>

      <header class="brand">
        <span class="brand-mark"></span>
        <div class="brand-name">BRIGHT KELP CO</div>
      </header>

      <h1 class="descriptor">
        <span class="line-1">Mineral</span>
        <span class="line-2">Hydration</span>
      </h1>

      <p class="subhead">Carbonated Electrolyte<br>Beverage with Sea Moss &amp;<br>Real Fruit Juice</p>

      <div class="fruit-art" role="img" aria-label="Flat drawing of a mango, a watermelon slice and mint leaves"></div>

      <h2 class="flavor">
        <span class="primary">Watermelon</span>
        <span class="secondary">Mint + <span class="mango">Mango</span></span>
      </h2>

      <ul class="badges">
        <li class="badge">
          <svg width="42" height="42" viewBox="0 0 42 42" aria-hidden="true">
            <circle cx="21" cy="21" r="19" fill="#ffffff" fill-opacity="0.85" stroke="#888" stroke-width="2"/>
            <path d="M21 30 V19 M21 22 C15 22 12 18 12 13 C17 13 21 16 21 22 M21 20 C21 15 25 12 30 12 C30 17 26 20 21 20" fill="none" stroke="#666" stroke-width="2"/>
          </svg>
          <div class="badge-text">PLANT<br>BASED</div>
        </li>
        <li class="badge">
          <svg width="42" height="42" viewBox="0 0 42 42" aria-hidden="true">
            <circle cx="21" cy="21" r="19" fill="#ffffff" fill-opacity="0.85" stroke="#888" stroke-width="2"/>
            <rect x="15" y="10" width="12" height="12" fill="#555"/>
            <path d="M21 23 V31 M17 27 L21 31 L25 27" fill="none" stroke="#555" stroke-width="2"/>
          </svg>
          <div class="badge-text">LOW IN<br>SUGAR</div>
        </li>
        <li class="badge">
          <svg width="42" height="42" viewBox="0 0 42 42" aria-hidden="true">
            <circle cx="21" cy="21" r="19" fill="#ffffff" fill-opacity="0.85" stroke="#888" stroke-width="2"/>
          </svg>
          <div class="badge-text">MADE WITH REAL<br>SEA MOSS</div>
        </li>
      </ul>

      <div class="volume">12 FL OZ (355mL)</div>
    </div>
  </div>
</body>
</html>
```